Diagramm/Grafik zur Darstellung einer Formel
Zielgruppe
Das Unternehmen ist in der Unternehmensberatung tätig und beschäftigt sich mit der Analyse von IT-In- und Outsourcing.
Zielgruppe: Entscheider / Höheres Management / Round Table
Aufgabenstellung
Es wurde für die Bewertung des bestehenden Outsourcing eine Formel entwickelt, welche es ermöglicht einerseits die Stärken
und Schwächen und andererseits die Entwicklung und Vorteilhaftigkeit der Kosten für die nächsten Jahre zu prognostizieren.
Der Name der Formel ist "MIRAX-P Methode" (Strategie, Technologie, Organisation, Qualität und Kosten)
Die Formel ist aufgebaut aus 5 Sektoren, unter welchem jeweils 3-8 Faktoren untergeordnet sind. (siehe IMG_1159)
Die Zuordnung der Faktoren zu Sektoren (siehe SektorenFaktoren.pdf) ist variabel, aus welchem Grund unter jedem Sektor 3-8 Faktoren unterordnenbar sein sollten.
Grundsätzlich findet die Auswertung aus dem Vergleich von Kosten + Risiken - Chancen jeweils von Outsourcing und Insourcing statt. (siehe IMG_1190)
Ziel ist es, eine Darstellung der Sektoren und Faktoren sowie der Formel zu finden, welche:
a) die Abhängigkeit von den Faktoren zu den Sektoren darstellt
b) die Formel darstellt
c) sich als Ganzes oder in Teilen für diverse Unterlagen verwenden lässt (bspw. .pptx, .pdf, etc.)
--> es ist geplant diese Darstellung bspw. als Ganzes oder in Teilen in eine PowerPoint-Präsentation zu integrieren
Diese Aufgabenstellung ist ein erster Versuch mittels der Plattform pixelhafen.de Aufträge zu vergeben.
Bei Erfolg sind Anschlussaufträge geplant.
WICHTIG: Alle Anhänge diesen lediglich zur Darstellung der Zusammenhänge, sollen aber keinerlei design vorgeben!

```html
<!DOCTYPE html>
<html lang="de">
<head>
<meta charset="utf-8">
<title>Die MIRAX-P Methode</title>
<link rel="stylesheet" href="https://fonts.googleapis.com/css2?family=Montserrat:wght@600;700&family=Barlow+Condensed:wght@300;400;500;600&family=Barlow:wght@400&display=swap">
<style>
  :root{
    --bg:#dadfe4;
    --orange:#e0510c;
    --orange-dark:#c9440a;
    --blue-light:#7089ab;
    --blue-dark:#2f4c74;
    --value:#8d9eb4;
    --row-border:#b9c3cf;
    --empty:#e3e7eb;
    --text:#1b1b1b;
    --white:#ffffff;
  }
  *{box-sizing:border-box;margin:0;padding:0}
  html,body{width:1200px;height:670px;overflow:hidden;background:var(--bg)}
  body{position:relative;font-family:"Barlow Condensed",sans-serif;color:var(--text)}

  .title-band{position:absolute;left:32px;top:31px;width:1135px;height:50px;background:var(--orange);border-radius:3px;
    display:flex;align-items:baseline;padding-left:72px;padding-top:8px;color:var(--white)}
  .title-band h1{font-family:"Montserrat",sans-serif;font-weight:700;font-size:33px;letter-spacing:.5px}
  .title-band .subtitle{font-family:"Barlow",sans-serif;font-size:20px;margin-left:10px;letter-spacing:.3px}

  .panel{position:absolute;left:0;width:1200px;height:220px}
  .panel.outsourcing{top:125px}
  .panel.insourcing{top:416px}

  .side-arrow{position:absolute;top:9px;width:53px;height:209px;background:var(--orange);
    clip-path:polygon(0 0,68% 0,100% 50%,68% 100%,0 100%);display:flex;align-items:center;justify-content:center}
  .side-arrow.left{left:32px}
  .side-arrow.right{left:1027px}
  .side-arrow span{writing-mode:vertical-rl;transform:rotate(180deg);color:var(--white);
    font-family:"Barlow",sans-serif;font-weight:400;font-size:27px;letter-spacing:2px;margin-right:10px}

  .sector{position:absolute;top:0;width:151px}
  .factor-label{position:absolute;right:0;top:0;font-size:10px;font-weight:600;color:#5d6b7d}
  .sector-head{position:absolute;left:0;top:9px;width:151px;height:20px;border-radius:2px;
    background:linear-gradient(90deg,var(--blue-light),var(--blue-dark) 70%);box-shadow:0 1px 2px rgba(0,0,0,.25);
    display:flex;justify-content:space-between;align-items:center;padding:0 6px;color:var(--white);
    font-weight:600;font-size:15px;letter-spacing:.8px}
  .sector-head::after{content:"";position:absolute;right:6px;top:24px;border:6px solid transparent;border-top:0;border-bottom:6px solid var(--value)}
  .rows{position:absolute;left:0;top:44px;width:151px;display:flex;flex-direction:column;gap:4.5px}
  .row{height:18px;display:flex;border:1px solid var(--row-border);background:var(--white);border-radius:2px;overflow:hidden}
  .row .name{flex:1;font-size:11px;padding-left:5px;line-height:16px;white-space:nowrap;overflow:hidden}
  .row .val{width:25px;background:var(--value);color:var(--white);font-size:11px;font-weight:500;text-align:center;line-height:16px}
  .row.empty{background:var(--empty);border-color:#f4f6f8}

  .plus{position:absolute;top:6px;width:24px;height:24px}

  .result{position:absolute;left:1093px;top:0;width:74px;text-align:center}
  .result .factor-label{position:static;display:block;color:var(--orange);font-size:10px}
  .result .score{font-weight:600;font-size:33px;color:var(--orange);line-height:1;margin-top:3px}
  .tag{position:absolute;left:0;width:74px;height:20px;background:linear-gradient(180deg,var(--orange),var(--orange-dark));
    color:var(--white);font-weight:600;font-size:15px;letter-spacing:1px;line-height:20px;padding-left:6px;text-align:left;
    border-radius:2px;box-shadow:0 1px 2px rgba(0,0,0,.2)}
  .tag.kosten{top:68px}.tag.risiken{top:104px}.tag.chancen{top:139px}

  .divider{position:absolute;left:34px;top:381px;width:1132px;height:4px;
    background:repeating-linear-gradient(90deg,var(--white) 0 9px,transparent 9px 19px)}
</style>
</head>
<body>

<header class="title-band">
  <h1>Die MIRAX-P Methode</h1>
  <span class="subtitle">(Strategie, Technologie, Organisation, Qualität und Kosten)</span>
</header>

<section class="panel outsourcing">
  <div class="side-arrow left"><span>OUTSOURCING</span></div>

  <div class="sector" style="left:103px">
    <span class="factor-label">Faktor</span>
    <div class="sector-head"><span>STRATEGIE</span><span>0,0</span></div>
    <div class="rows">
      <div class="row"><span class="name">komparativer Konkurrenzvorteil</span><span class="val">0,0</span></div>
      <div class="row"><span class="name">Kernkompetenz</span><span class="val">0,0</span></div>
      <div class="row"><span class="name">Wertschöpfungstiefe</span><span class="val">0,0</span></div>
      <div class="row"><span class="name">Marktbewegung</span><span class="val">0,0</span></div>
      <div class="row"><span class="name">Marktein-/-austrittsstrategie</span><span class="val">0,0</span></div>
      <div class="row"><span class="name">Sourcing-/Vendorstrategie</span><span class="val">0,0</span></div>
      <div class="row"><span class="name">Risikoabsicherung</span><span class="val">0,0</span></div>
      <div class="row"><span class="name">Ungewissheit</span><span class="val">0,0</span></div>
    </div>
  </div>
  <svg class="plus" style="left:261px" viewBox="0 0 24 24"><circle cx="12" cy="12" r="12" fill="#e0510c"/><path d="M12 6v12M6 12h12" stroke="#fff" stroke-width="3.4"/></svg>

  <div class="sector" style="left:293px">
    <span class="factor-label">Faktor</span>
    <div class="sector-head"><span>TECHNOLOGIE</span><span>0,0</span></div>
    <div class="rows">
      <div class="row"><span class="name">Innovationsrate</span><span class="val">0,0</span></div>
      <div class="row"><span class="name">Synergien</span><span class="val">0,0</span></div>
      <div class="row"><span class="name">Portfolio-Erweiterung</span><span class="val">0,0</span></div>
      <div class="row"><span class="name">Best-Practices</span><span class="val">0,0</span></div>
      <div class="row empty"></div><div class="row empty"></div><div class="row empty"></div><div class="row empty"></div>
    </div>
  </div>
  <svg class="plus" style="left:450px" viewBox="0 0 24 24"><circle cx="12" cy="12" r="12" fill="#e0510c"/><path d="M12 6v12M6 12h12" stroke="#fff" stroke-width="3.4"/></svg>

  <div class="sector" style="left:482px">
    <span class="factor-label">Faktor</span>
    <div class="sector-head"><span>ORGANISATION</span><span>0,0</span></div>
    <div class="rows">
      <div class="row"><span class="name">Wissen</span><span class="val">0,0</span></div>
      <div class="row"><span class="name">Kommunikation</span><span class="val">0,0</span></div>
      <div class="row"><span class="name">Umsetzungsgeschwindigkeit</span><span class="val">0,0</span></div>
      <div class="row"><span class="name">Flexibilität</span><span class="val">0,0</span></div>
      <div class="row"><span class="name">Skalierbarkeit</span><span class="val">0,0</span></div>
      <div class="row"><span class="name">Time-to-Market</span><span class="val">0,0</span></div>
      <div class="row"><span class="name">Organisationstransformation</span><span class="val">0,0</span></div>
      <div class="row empty"></div>
    </div>
  </div>
  <svg class="plus" style="left:640px" viewBox="0 0 24 24"><circle cx="12" cy="12" r="12" fill="#e0510c"/><path d="M12 6v12M6 12h12" stroke="#fff" stroke-width="3.4"/></svg>

  <div class="sector" style="left:672px">
    <span class="factor-label">Faktor</span>
    <div class="sector-head"><span>QUALITÄT</span><span>0,0</span></div>
    <div class="rows">
      <div class="row"><span class="name">Kontroll- und Prüfaufwände</span><span class="val">0,0</span></div>
      <div class="row"><span class="name">Compliance (legal)</span><span class="val">0,0</span></div>
      <div class="row"><span class="name">Sprach- /Kulturbarrieren</span><span class="val">0,0</span></div>
      <div class="row"><span class="name">Distanz/Nähe</span><span class="val">0,0</span></div>
      <div class="row empty"></div><div class="row empty"></div><div class="row empty"></div><div class="row empty"></div>
    </div>
  </div>
  <svg class="plus" style="left:829px" viewBox="0 0 24 24"><circle cx="12" cy="12" r="12" fill="#e0510c"/><path d="M12 6v12M6 12h12" stroke="#fff" stroke-width="3.4"/></svg>

  <div class="sector" style="left:861px">
    <span class="factor-label">Faktor</span>
    <div class="sector-head"><span>KOSTEN</span><span>0,0</span></div>
    <div class="rows">
      <div class="row"><span class="name">Management</span><span class="val">0,0</span></div>
      <div class="row"><span class="name">Vertragsänderung/-verwaltung</span><span class="val">0,0</span></div>
      <div class="row"><span class="name">Cash Flow</span><span class="val">0,0</span></div>
      <div class="row"><span class="name">Return-on-Invest</span><span class="val">0,0</span></div>
      <div class="row"><span class="name">fixe vs. Variable Kosten</span><span class="val">0,0</span></div>
      <div class="row"><span class="name">Tax</span><span class="val">0,0</span></div>
      <div class="row empty"></div><div class="row empty"></div>
    </div>
  </div>

  <div class="side-arrow right"><span>ERGEBNIS</span></div>

  <div class="result">
    <span class="factor-label">Faktor</span>
    <div class="score">00,0</div>
    <div class="tag kosten">KOSTEN</div>
    <div class="tag risiken">RISIKEN</div>
    <div class="tag chancen">CHANCEN</div>
  </div>
</section>

<div class="divider"></div>

<section class="panel insourcing">
  <div class="side-arrow left"><span>INSOURCING</span></div>

  <div class="sector" style="left:103px">
    <span class="factor-label">Faktor</span>
    <div class="sector-head"><span>STRATEGIE</span><span>0,0</span></div>
    <div class="rows">
      <div class="row"><span class="name">komparativer Konkurrenzvorteil</span><span class="val">0,0</span></div>
      <div class="row"><span class="name">Kernkompetenz</span><span class="val">0,0</span></div>
      <div class="row"><span class="name">Wertschöpfungstiefe</span><span class="val">0,0</span></div>
      <div class="row"><span class="name">Marktbewegung</span><span class="val">0,0</span></div>
      <div class="row"><span class="name">Marktein-/-austrittsstrategie</span><span class="val">0,0</span></div>
      <div class="row"><span class="name">Sourcing-/Vendorstrategie</span><span class="val">0,0</span></div>
      <div class="row"><span class="name">Risikoabsicherung</span><span class="val">0,0</span></div>
      <div class="row"><span class="name">Ungewissheit</span><span class="val">0,0</span></div>
    </div>
  </div>
  <svg class="plus" style="left:261px" viewBox="0 0 24 24"><circle cx="12" cy="12" r="12" fill="#e0510c"/><path d="M12 6v12M6 12h12" stroke="#fff" stroke-width="3.4"/></svg>

  <div class="sector" style="left:293px">
    <span class="factor-label">Faktor</span>
    <div class="sector-head"><span>TECHNOLOGIE</span><span>0,0</span></div>
    <div class="rows">
      <div class="row"><span class="name">Innovationsrate</span><span class="val">0,0</span></div>
      <div class="row"><span class="name">Synergien</span><span class="val">0,0</span></div>
      <div class="row"><span class="name">Portfolio-Erweiterung</span><span class="val">0,0</span></div>
      <div class="row"><span class="name">Best-Practices</span><span class="val">0,0</span></div>
      <div class="row empty"></div><div class="row empty"></div><div class="row empty"></div><div class="row empty"></div>
    </div>
  </div>
  <svg class="plus" style="left:450px" viewBox="0 0 24 24"><circle cx="12" cy="12" r="12" fill="#e0510c"/><path d="M12 6v12M6 12h12" stroke="#fff" stroke-width="3.4"/></svg>

  <div class="sector" style="left:482px">
    <span class="factor-label">Faktor</span>
    <div class="sector-head"><span>ORGANISATION</span><span>0,0</span></div>
    <div class="rows">
      <div class="row"><span class="name">Wissen</span><span class="val">0,0</span></div>
      <div class="row"><span class="name">Kommunikation</span><span class="val">0,0</span></div>
      <div class="row"><span class="name">Umsetzungsgeschwindigkeit</span><span class="val">0,0</span></div>
      <div class="row"><span class="name">Flexibilität</span><span class="val">0,0</span></div>
      <div class="row"><span class="name">Skalierbarkeit</span><span class="val">0,0</span></div>
      <div class="row"><span class="name">Time-to-Market</span><span class="val">0,0</span></div>
      <div class="row"><span class="name">Organisationstransformation</span><span class="val">0,0</span></div>
      <div class="row empty"></div>
    </div>
  </div>
  <svg class="plus" style="left:640px" viewBox="0 0 24 24"><circle cx="12" cy="12" r="12" fill="#e0510c"/><path d="M12 6v12M6 12h12" stroke="#fff" stroke-width="3.4"/></svg>

  <div class="sector" style="left:672px">
    <span class="factor-label">Faktor</span>
    <div class="sector-head"><span>QUALITÄT</span><span>0,0</span></div>
    <div class="rows">
      <div class="row"><span class="name">Kontroll- und Prüfaufwände</span><span class="val">0,0</span></div>
      <div class="row"><span class="name">Compliance (legal)</span><span class="val">0,0</span></div>
      <div class="row"><span class="name">Sprach- /Kulturbarrieren</span><span class="val">0,0</span></div>
      <div class="row"><span class="name">Distanz/Nähe</span><span class="val">0,0</span></div>
      <div class="row empty"></div><div class="row empty"></div><div class="row empty"></div><div class="row empty"></div>
    </div>
  </div>
  <svg class="plus" style="left:829px" viewBox="0 0 24 24"><circle cx="12" cy="12" r="12" fill="#e0510c"/><path d="M12 6v12M6 12h12" stroke="#fff" stroke-width="3.4"/></svg>

  <div class="sector" style="left:861px">
    <span class="factor-label">Faktor</span>
    <div class="sector-head"><span>KOSTEN</span><span>0,0</span></div>
    <div class="rows">
      <div class="row"><span class="name">Management</span><span class="val">0,0</span></div>
      <div class="row"><span class="name">Vertragsänderung/-verwaltung</span><span class="val">0,0</span></div>
      <div class="row"><span class="name">Cash Flow</span><span class="val">0,0</span></div>
      <div class="row"><span class="name">Return-on-Invest</span><span class="val">0,0</span></div>
      <div class="row"><span class="name">fixe vs. Variable Kosten</span><span class="val">0,0</span></div>
      <div class="row"><span class="name">Tax</span><span class="val">0,0</span></div>
      <div class="row empty"></div><div class="row empty"></div>
    </div>
  </div>

  <div class="side-arrow right"><span>ERGEBNIS</span></div>

  <div class="result">
    <span class="factor-label">Faktor</span>
    <div class="score">00,0</div>
    <div class="tag kosten">KOSTEN</div>
    <div class="tag risiken">RISIKEN</div>
    <div class="tag chancen">CHANCEN</div>
  </div>
</section>

</body>
</html>
```